GUARANTEED! Simple website for independent event planner and consultant...

I need a website that is no more than 5 or 6 pages to illustrate who I am and what I can offer to groups who book hotels for meetings and conferences. I have 20 years of experience planning meetings within hotels and I am now ready to go out on my own and help clients choose venues, negotiate contracts and plan effective meetings. I will focus on clients planning meetings in the mountains of Colorado but I am willing to travel as well. I want to work with a person who is collaborative and can direct me on what they need to move the project along quickly. I already have my logo, a hosting site and work e-mail address. Also, I recently hired a photographer to do head shots. Lastly, it important for me to be able to talk on the phone or skype with this person, as needed and I must be able to make changes to my site down the road when necessary...

Target Market(s)

Corporate Groups

Industry/Entity Type

Event Planning

Coding

Coded - Design and coding required

Number of Pages Required

5+ page

Font styles to use
Sans Serif

Requirements
Must have
• About me page, event planning services offered page, task force and consulting work page, testimonials page, page for blogs, page to contact me/request a proposal. May need advice on what else I need...
Nice to have
• I want it to look sharp and professional. I want people to look at my site and know immediately that they can trust me and the work I can do.
• I don't want it to look like it is over the top as I am not a HUGE company but I do want it to be professional and easy to view and navigate.
Should not have
• Bright colors
• My logo is bright orange and black. I have also used dark grey and orange. See below:
• Orange:
• C = 0
• M = 64
• Y = 100
• K = 0
• Gray:
• C = 67
• M = 60
• Y = 59
• K = 45
• Font: Gotham Book and Gotham Bold

```html
<!DOCTYPE html>
<html lang="en">
<head>
<meta charset="utf-8">
<title>Alder Event Management</title>
<link href="https://fonts.googleapis.com/css2?family=Montserrat:wght@400;500;600;700&family=Open+Sans:wght@400;600&display=swap" rel="stylesheet">
<style>
:root{
  --orange:#f47b20;
  --charcoal:#3a3a3c;
  --ink:#2b2b2b;
  --grey:#6d6d6d;
  --cream:#fdf5ec;
  --white:#ffffff;
}
*{box-sizing:border-box;margin:0;padding:0}
html,body{width:1200px;height:3480px;overflow:hidden}
body{position:relative;font-family:"Open Sans",Arial,sans-serif;color:var(--grey);background:var(--white)}
.abs{position:absolute}
h1,h2,h3,h4,.nav,.btn,.caption,.brand,.hero-title{font-family:"Montserrat",Arial,sans-serif}

/* hero */
.hero{left:0;top:0;width:1200px;height:740px;background:linear-gradient(180deg,#5d6066 0%,#8b8e93 45%,#a9abae 70%,#6f7175 100%)}
.brand{left:100px;top:38px;color:var(--white);font-weight:600;font-size:17px;letter-spacing:1px;text-transform:uppercase}
.nav{right:80px;top:38px;display:flex;gap:10px}
.nav a{color:var(--white);text-decoration:none;font-size:14px;font-weight:500;padding:9px 18px}
.nav a.active{background:var(--orange);border:2px solid var(--white)}
.hero-title{left:0;top:300px;width:1200px;text-align:center;color:var(--white);font-weight:600;font-size:30px;line-height:1.3;letter-spacing:2px;text-transform:uppercase}
.hero-dots{left:530px;top:680px;display:flex;gap:8px}
.hero-dots i{display:block;width:40px;height:5px;background:rgba(255,255,255,.6)}
.hero-dots i.on{background:var(--orange)}

/* about */
.portrait{left:780px;top:700px;width:420px;height:620px;background:linear-gradient(160deg,#f2f2f2 0%,#cfcfcf 55%,#5a5a5a 100%)}
.about{left:100px;top:850px;width:640px}
.about h2{color:var(--orange);font-size:31px;font-weight:600}
.about h3{color:var(--ink);font-size:18px;font-weight:500;margin:10px 0 26px}
.about p{font-size:14px;line-height:1.65;margin-bottom:16px}
.btn{display:inline-block;background:var(--orange);color:var(--white);font-size:14px;font-weight:500;padding:12px 22px}

/* process */
.process{left:0;top:1320px;width:1200px;height:520px;background:var(--cream)}
.section-title{width:1200px;text-align:center;font-family:"Montserrat",Arial,sans-serif;font-size:26px;font-weight:600;color:var(--orange)}
.section-title::after{content:"";display:block;width:60px;height:2px;background:var(--orange);margin:14px auto 0}
.intro{left:250px;width:700px;text-align:center;font-size:14px;line-height:1.65}
.step{width:320px;display:flex;gap:18px}
.step .ico{flex:none;width:64px;height:64px;border:2px solid var(--charcoal);display:flex;align-items:center;justify-content:center}
.step .ico.hot{background:var(--orange);border-color:var(--orange)}
.step h4{font-size:18px;font-weight:500;color:var(--ink);margin-bottom:10px}
.step h4.hot{color:var(--orange)}
.step p{font-size:12.5px;line-height:1.55}
.more{display:inline-block;margin-top:18px;border:1px solid var(--charcoal);font-size:12px;color:var(--ink);padding:5px 14px;font-family:"Montserrat",Arial,sans-serif}

/* company band */
.band{left:0;top:1780px;width:1200px;height:700px;background:var(--orange);clip-path:polygon(0 60px,100% 0,100% 100%,0 calc(100% - 50px))}
.band-title{color:var(--white)}
.band-title::after{background:var(--white)}
.band-intro{color:var(--white)}
.card{width:320px;height:260px;top:2080px;background:linear-gradient(135deg,#c9b8a6,#7c6f66)}
.card.alt{background:linear-gradient(135deg,#b8bcc3,#5a5e66)}
.card .caption{position:absolute;left:0;bottom:0;width:100%;height:52px;background:rgba(30,30,30,.85);color:var(--white);font-size:15px;font-weight:500;text-transform:uppercase;display:flex;align-items:center;justify-content:center;letter-spacing:.5px}
.band-dots{left:480px;top:2390px;display:flex;gap:8px}
.band-dots i{display:block;width:72px;height:5px;background:rgba(255,255,255,.55)}
.band-dots i.on{background:var(--white)}

/* specialties */
.spec{top:2660px;width:180px;text-align:center}
.spec .ring{width:128px;height:128px;margin:0 auto;border:2px solid var(--charcoal);border-radius:50%;display:flex;align-items:center;justify-content:center}
.spec .ring.hot{background:var(--orange);border-color:var(--orange)}
.spec p{margin-top:18px;font-family:"Montserrat",Arial,sans-serif;font-size:14px;font-weight:500;color:var(--ink)}
.spec p.hot{color:var(--orange)}

/* footer */
.footer{left:0;top:2940px;width:1200px;height:540px;background:var(--charcoal);color:#d8d8d8}
.footer h4{color:var(--white);font-size:22px;font-weight:500}
.contact-row{display:flex;gap:18px;align-items:flex-start;font-size:13.5px;line-height:1.5}
.contact-row .dot{flex:none;width:40px;height:40px;border-radius:50%;border:2px solid var(--orange);display:flex;align-items:center;justify-content:center}
.field{width:310px;height:40px;border:1px solid #9a9a9a;padding:10px 14px;font-size:13px;color:#d0d0d0}
.field.area{height:100px}
.subscribe{background:var(--orange);color:var(--white);width:310px;height:40px;display:flex;align-items:center;justify-content:center;font-family:"Montserrat",Arial,sans-serif;font-size:13px;font-weight:600;text-transform:uppercase}
.rule{left:100px;top:3410px;width:1000px;height:1px;background:#555}
.copyright{left:100px;top:3432px;font-size:12px;color:#cfcfcf}
.social{left:940px;top:3426px;display:flex;gap:8px}
.social i{display:block;width:26px;height:26px;border:1px solid #bbb;border-radius:50%}
.top-link{left:1110px;top:3430px;font-size:12px;color:#cfcfcf}
</style>
</head>
<body>

<!-- hero -->
<div class="abs hero" role="img" aria-label="Modern glass-walled conference room with a long table and chairs"></div>
<div class="abs brand">Alder Event Management</div>
<nav class="abs nav">
  <a class="active" href="#">Home</a><a href="#">About Us</a><a href="#">Our Events</a><a href="#">Gallery</a><a href="#">Contact Us</a>
</nav>
<h1 class="abs hero-title">Alder<br>Event Management</h1>
<div class="abs hero-dots"><i class="on"></i><i></i><i></i></div>
<svg class="abs" style="left:0;top:660px" width="1200" height="100" viewBox="0 0 1200 100">
  <polygon points="0,40 1200,0 1200,60 0,100" fill="#f47b20"/>
  <polygon points="0,100 1200,60 1200,100" fill="#ffffff"/>
</svg>

<!-- about -->
<div class="abs portrait" role="img" aria-label="Black and white head shot of the event planner in a dark blazer"></div>
<section class="abs about">
  <h2>Dana Mercer, CMP, CMM</h2>
  <h3>Event planner and consultant</h3>
  <p>With two decades spent planning meetings inside hotels, I help groups find the right venue, agree fair terms and run sessions that feel effortless. Every project gets careful attention to timing, budget and the small details that make guests feel welcome from arrival to departure.</p>
  <p>Based in the mountains of Colorado and happy to travel, I work closely with each client so plans move quickly and decisions stay simple.</p>
  <span class="btn">Read More</span>
</section>

<!-- process -->
<div class="abs process"></div>
<h2 class="abs section-title" style="left:0;top:1440px">OUR PROCESS</h2>
<p class="abs intro" style="top:1510px">Alder Event Management specializes in event management for associations, corporations, not for profit companies and personal social events of all sizes in the state of Colorado.</p>

<div class="abs step" style="left:100px;top:1620px">
  <div class="ico hot"><svg width="30" height="30" viewBox="0 0 24 24" fill="none" stroke="#fff" stroke-width="2"><path d="M12 22s7-7 7-12a7 7 0 0 0-14 0c0 5 7 12 7 12z"/><circle cx="12" cy="10" r="2.5"/></svg></div>
  <div><h4 class="hot">Choose Venues</h4><p>We match your group with hotels that fit your dates, size and budget.</p><span class="more">More Info</span></div>
</div>
<div class="abs step" style="left:445px;top:1620px">
  <div class="ico"><svg width="30" height="30" viewBox="0 0 24 24" fill="none" stroke="#3a3a3c" stroke-width="1.8"><rect x="5" y="3" width="14" height="18"/><path d="M8 8h8M8 12h8M8 16h5"/></svg></div>
  <div><h4>Negotiate Contracts</h4><p>We secure clear terms and fair rates so there are no surprises later.</p><span class="more">More Info</span></div>
</div>
<div class="abs step" style="left:790px;top:1620px">
  <div class="ico"><svg width="30" height="30" viewBox="0 0 24 24" fill="none" stroke="#3a3a3c" stroke-width="1.8"><rect x="3" y="5" width="18" height="16"/><path d="M3 10h18M8 3v4M16 3v4"/></svg></div>
  <div><h4>Plan Effective Meetings</h4><p>We shape agendas and logistics so every session runs on time.</p><span class="more">More Info</span></div>
</div>

<!-- company band -->
<div class="abs band"></div>
<h2 class="abs section-title band-title" style="left:0;top:1912px">ALDER EVENT MANAGEMENT</h2>
<p class="abs intro band-intro" style="top:1985px">After a successful 20 year career coordinating events in the corporate world, our team is now providing services across the state. Whether you need a venue or full planning, Alder Event Management is here to help your company.</p>
<div class="abs card" style="left:100px" role="img" aria-label="Hotel meeting room set with tables"><div class="caption">Hotels for Meetings</div></div>
<div class="abs card alt" style="left:440px" role="img" aria-label="Business people talking at a conference"><div class="caption">Conferences</div></div>
<div class="abs card alt" style="left:780px" role="img" aria-label="Audience seated at a planning seminar"><div class="caption">Planning Consultants</div></div>
<div class="abs band-dots"><i class="on"></i><i></i><i></i></div>

<!-- specialties -->
<h2 class="abs section-title" style="left:0;top:2570px">OUR SPECIALTIES</h2>
<svg class="abs" style="left:36px;top:2706px" width="20" height="36" viewBox="0 0 20 36"><path d="M16 2 4 18l12 16" fill="none" stroke="#3a3a3c" stroke-width="2.5"/></svg>
<svg class="abs" style="left:1144px;top:2706px" width="20" height="36" viewBox="0 0 20 36"><path d="M4 2l12 16L4 34" fill="none" stroke="#3a3a3c" stroke-width="2.5"/></svg>

<div class="abs spec" style="left:78px"><div class="ring"><svg width="46" height="46" viewBox="0 0 24 24" fill="none" stroke="#3a3a3c" stroke-width="1.5"><path d="M12 20s6-6 6-10.5a6 6 0 0 0-12 0C6 14 12 20 12 20z"/><circle cx="12" cy="9.5" r="2.2"/><path d="M7 20h10"/></svg></div><p>Venue Selection</p></div>
<div class="abs spec" style="left:298px"><div class="ring hot"><svg width="46" height="46" viewBox="0 0 24 24" fill="none" stroke="#fff" stroke-width="1.5"><rect x="6" y="3" width="12" height="17"/><path d="M9 8h6M9 11h6M9 14h4"/><path d="M4 6v16h12"/></svg></div><p class="hot">Contract Negotiations</p></div>
<div class="abs spec" style="left:510px"><div class="ring"><svg width="46" height="46" viewBox="0 0 24 24" fill="none" stroke="#3a3a3c" stroke-width="1.5"><path d="M4 17a8 8 0 0 1 16 0z"/><path d="M2 19h20M12 9V7"/><circle cx="12" cy="6" r="1"/></svg></div><p>Food and Beverage</p></div>
<div class="abs spec" style="left:710px"><div class="ring"><svg width="46" height="46" viewBox="0 0 24 24" fill="none" stroke="#3a3a3c" stroke-width="1.5"><rect x="3" y="5" width="18" height="16"/><path d="M3 10h18M8 3v4M16 3v4M7 13h2M11 13h2M15 13h2M7 17h2M11 17h2"/></svg></div><p>Agenda Creation</p></div>
<div class="abs spec" style="left:930px"><div class="ring"><svg width="46" height="46" viewBox="0 0 24 24" fill="none" stroke="#3a3a3c" stroke-width="1.6"><path d="M9 18V5l11-2v13"/><circle cx="6.5" cy="18" r="2.5"/><circle cx="17.5" cy="16" r="2.5"/></svg></div><p>Audio/Visual Expertise</p></div>

<!-- footer -->
<footer class="abs footer">
  <h4 class="abs" style="left:100px;top:60px">Contact Us:</h4>
  <div class="abs contact-row" style="left:100px;top:120px">
    <span class="dot"><svg width="18" height="18" viewBox="0 0 24 24" fill="none" stroke="#f47b20" stroke-width="2"><rect x="3" y="6" width="18" height="12"/><path d="M3 6l9 7 9-7"/></svg></span>
    <span style="padding-top:10px">info@aldereventmanagement.com</span>
  </div>
  <div class="abs contact-row" style="left:100px;top:190px">
    <span class="dot"><svg width="18" height="18" viewBox="0 0 24 24" fill="none" stroke="#f47b20" stroke-width="2"><path d="M12 21s6-6 6-11a6 6 0 0 0-12 0c0 5 6 11 6 11z"/><circle cx="12" cy="10" r="2"/></svg></span>
    <span>PO Box 1200 Ridgeview, CO 80000<br>United States</span>
  </div>
  <div class="abs contact-row" style="left:100px;top:270px">
    <span class="dot"><svg width="18" height="18" viewBox="0 0 24 24" fill="none" stroke="#f47b20" stroke-width="2"><path d="M5 3h4l2 5-3 2a11 11 0 0 0 6 6l2-3 5 2v4a2 2 0 0 1-2 2A17 17 0 0 1 3 5a2 2 0 0 1 2-2z"/></svg></span>
    <span style="padding-top:10px">+1 555 010 2536</span>
  </div>

  <h4 class="abs" style="left:460px;top:60px">Contact Form:</h4>
  <div class="abs field" style="left:460px;top:110px">Name</div>
  <div class="abs field" style="left:460px;top:165px">Email</div>
  <div class="abs field" style="left:460px;top:220px">Phone Number</div>
  <div class="abs field area" style="left:790px;top:110px">Message</div>
  <div class="abs subscribe" style="left:790px;top:220px">Subscribe Now</div>
</footer>
<div class="abs rule"></div>
<div class="abs copyright">Copyright © 2017 Alder Event Management. All Rights Reserved.</div>
<div class="abs social"><i></i><i></i><i></i><i></i></div>
<div class="abs top-link">∧ Top</div>

</body>
</html>
```